Business Card for a mobile physiotherapy company

I need a layout for a business card for a mobile physiotherapy company.
Slogan is "Mobile Physiotherapy - Your Road To Recovery"
Phone number is 867-402-5913
Email VantrePhysio@mailbright.ca (subject to change with website)
Website www.VantrePhysio.ca
My name and credentials: Kent Vantre Kent Vantre, BSc(kin), MPT, CAFCI, IMS
Information maybe included: Direct Billing, Services including Physiotherapy, IMS, acupuncture
Maybe include facebook and instagram logos
One side with the logo clean and sharp
Other side with details, try not to look too busy, keep everything concise

```html
<!DOCTYPE html>
<html lang="en">
<head>
<meta charset="utf-8">
<title>Vantre Therapy – Business Card</title>
<link rel="stylesheet" href="https://fonts.googleapis.com/css2?family=Bebas+Neue&family=Lato:ital,wght@0,400;1,400;1,700&display=swap">
<style>
  :root {
    --backdrop: #5f5048;
    --navy: #2c4a72;
    --navy-deep: #233f66;
    --green: #1d5e4c;
    --silver: #b8bcc0;
    --paper: #f4f4f4;
    --ink-grey: #6c6c6c;
    --white: #ffffff;
  }
  * { margin: 0; padding: 0; box-sizing: border-box; }
  html, body { width: 1200px; height: 960px; overflow: hidden; }
  body {
    position: relative;
    background: var(--backdrop);
    font-family: "Lato", sans-serif;
  }
  .card {
    position: absolute;
    width: 615px;
    height: 351px;
    left: 295px;
  }
  .card-front {
    top: 104px;
    background: var(--navy);
    display: flex;
    align-items: center;
    justify-content: center;
  }
  .brand-name {
    font-family: "Lato", sans-serif;
    font-weight: 400;
    font-size: 44px;
    color: var(--silver);
    line-height: 1;
  }

  .card-back {
    top: 508px;
    background: var(--paper);
    overflow: hidden;
  }
  .identity {
    position: absolute;
    right: 47px;
    top: 57px;
    text-align: right;
  }
  .identity .person {
    font-family: "Bebas Neue", sans-serif;
    font-weight: 400;
    font-size: 28px;
    color: var(--navy);
    line-height: 1;
  }
  .identity .credentials {
    font-size: 14px;
    color: var(--ink-grey);
    margin-top: 0;
    line-height: 16px;
  }
  .services {
    position: absolute;
    left: 59px;
    top: 133px;
    list-style: none;
    font-size: 14.5px;
    color: var(--ink-grey);
    line-height: 18px;
  }
  .services .dot { color: var(--navy); font-size: 10px; margin-right: 1px; }
  .divider {
    position: absolute;
    left: 60px;
    top: 200px;
    width: 17px;
    height: 2px;
    background: var(--navy);
  }
  .contacts {
    position: absolute;
    left: 59px;
    top: 217px;
    list-style: none;
    font-size: 14.5px;
    color: var(--ink-grey);
    line-height: 18px;
  }
  .contacts li { display: flex; align-items: center; gap: 7px; }
  .contacts svg { width: 11px; height: 11px; flex: none; }
  .social-mark { width: 10px; height: 10px; border-radius: 50%; background: var(--navy); flex: none; }
  .swoosh { position: absolute; left: 0; top: 0; width: 615px; height: 351px; }
  .tagline {
    position: absolute;
    right: 35px;
    bottom: 11px;
    font-size: 14px;
    font-style: italic;
    color: var(--white);
  }
  .tagline strong { font-weight: 700; }
</style>
</head>
<body>

<section class="card card-front">
  <h1 class="brand-name">Vantre Therapy</h1>
</section>

<section class="card card-back">
  <svg class="swoosh" viewBox="0 0 615 351" aria-hidden="true">
    <path d="M34 351 Q 230 296 560 300 Q 250 304 52 351 Z" fill="var(--green)"/>
    <path d="M44 351 Q 240 306 615 312 L615 351 Z" fill="var(--navy-deep)"/>
  </svg>

  <div class="identity">
    <h2 class="person">KENT VANTRE KENT VANTRE</h2>
    <p class="credentials">BSc (kin), MPT, CAFCI, IMS</p>
  </div>

  <ul class="services">
    <li><span class="dot">●</span> Direct Billing</li>
    <li><span class="dot">●</span> Services including Physiotherapy</li>
    <li><span class="dot">●</span> IMS <span class="dot">●</span> Acupuncture</li>
  </ul>

  <div class="divider"></div>

  <ul class="contacts">
    <li>
      <svg viewBox="0 0 12 12"><path d="M2.5 1 L4.5 1 L5.3 3.4 L4 4.4 Q5 6.8 7.6 8 L8.6 6.7 L11 7.5 L11 9.5 Q10.5 11 9 11 Q1 10 1 2.5 Q1 1 2.5 1 Z" fill="var(--navy)"/></svg>
      867-402-5913
    </li>
    <li>
      <svg viewBox="0 0 12 12"><rect x="0.8" y="2.3" width="10.4" height="7.4" fill="none" stroke="var(--navy)" stroke-width="1.3"/><path d="M1 2.6 L6 6.6 L11 2.6" fill="none" stroke="var(--navy)" stroke-width="1.2"/></svg>
      VantrePhysio@mailbright.ca
    </li>
    <li>
      <svg viewBox="0 0 12 12"><circle cx="6" cy="6" r="5" fill="none" stroke="var(--navy)" stroke-width="1.1"/><ellipse cx="6" cy="6" rx="2.2" ry="5" fill="none" stroke="var(--navy)" stroke-width="1"/><path d="M1 6 H11 M2 3.4 H10 M2 8.6 H10" stroke="var(--navy)" stroke-width="0.9"/></svg>
      www.VantrePhysio.ca
    </li>
    <li>
      <span class="social-mark"></span>
      VantreTherapy
    </li>
  </ul>

  <p class="tagline"><strong>Mobile Physiotherapy</strong> - Your Road To Recovery</p>
</section>

</body>
</html>
```